Vendor Managed Inventory Talking points/Customer hand out

Looking for a single page flyer/Customer handout to be a sell sheet for our Vendor managed Inventory programs
Title: VMI benefits
Risk management:
Identification of Items and values that are sole sourced
Ongoing plans to reduce exposure to sole sourced items
Schedule planning to eliminate freight and outages
Reducing the hidden costs of forecasting errors
(Note; with us managing the point of use we can more accurately forecast)
Managing ever shortening of product lifecycles, minimizing obsolescence
Zero Inventory Exposure:
Minimized or Zero inventory on commodity items
Greatly reducing the Weighted Cost of Capital (WACC)
Reduced WACC can help in calculating Hurdle Rates
True point of use billing:
Allows for better tracking and allocation of expenses from a job-job basis
Custom labeling:
Including things like customer part numbers, exp dates, internal hazmat codes
Insures accurate processes with current materials
Helps to meet 5S requirements
Required for certain audits
Lot tracking/Shelf life:
Active assistance in managing Date Codes/Lot Tracking
Shortened shelf life products identified and managed
Plain statement of expiration dates on products. Calculations are not required
Taken as a whole we can help calculate TRUE management and landed costs of products. Focusing only on the price of items is like looking at just the exposed part of an iceberg. Let RQ7T help you to see what's underneath.
I have attached some other brochures and flyers for style reference
more info on our website too. www.rq7t-example.com
Target Market(s)
Electronics manufacturers
Industry/Entity Type
Electronics
Look and feel

```html
<!DOCTYPE html>
<html lang="en">
<head>
<meta charset="utf-8">
<title>VMI Benefits – RQ7T</title>
<link rel="stylesheet" href="https://fonts.googleapis.com/css2?family=Source+Sans+3:wght@400;600;700;800&display=swap">
<style>
  :root{
    --ink:#1a1a1a;
    --brand-blue:#1f7fc4;
    --title-navy:#2b3590;
    --panel:#f1f1f2;
    --c1:#3c6e8e; --c1-dark:#2f5c79; --c1-ring:#5f8fae;
    --c2:#fcc72c; --c2-dark:#f2ad14; --c2-ring:#f6b51e; --c2-head:#f0a81c;
    --c3:#3aa99a; --c3-dark:#2c8f82; --c3-ring:#52b9ab;
    --c4:#e0405e; --c4-dark:#c8304d; --c4-ring:#e65a74;
    --c5:#2b3590; --c5-dark:#242c7a; --c5-ring:#1f7fc4;
    --band:#1f7fc4;
    --footer:#111;
  }
  *{box-sizing:border-box;margin:0;padding:0}
  html,body{width:848px;height:1200px;overflow:hidden;background:#fff}
  body{font-family:"Source Sans 3",Arial,sans-serif;color:var(--ink);position:relative}

  .header{position:absolute;left:0;top:0;width:848px;height:160px}
  .brand{position:absolute;left:28px;top:22px;width:330px}
  .brand-mark{display:flex;align-items:center;gap:14px;height:72px}
  .brand-dot{width:46px;height:46px;border-radius:50%;background:var(--brand-blue)}
  .brand-name{font-size:64px;font-weight:800;color:var(--brand-blue);line-height:1;letter-spacing:1px}
  .brand-company{font-size:20px;font-weight:600;color:var(--ink);letter-spacing:.2px;margin-top:10px;white-space:nowrap}
  .brand-tagline{font-size:20px;font-weight:600;color:var(--brand-blue);letter-spacing:.4px;white-space:nowrap}

  .contact{position:absolute;font-size:15px;font-weight:700;color:var(--title-navy);display:flex;align-items:center;gap:9px;line-height:1.1;white-space:nowrap}
  .contact .icon{width:30px;height:30px;border-radius:50%;background:var(--ink);display:flex;align-items:center;justify-content:center;flex:none}
  .contact-web{left:390px;top:40px}
  .contact-mail{left:390px;top:92px}
  .contact-addr{left:634px;top:36px}
  .contact-phone{left:634px;top:92px}

  .rule-thick{position:absolute;left:0;top:160px;width:848px;height:9px;background:var(--footer)}
  .rule-thin{position:absolute;left:0;top:173px;width:848px;height:2px;background:var(--footer)}

  .title{position:absolute;left:0;top:180px;width:848px;text-align:center;font-size:44px;line-height:1;font-weight:400;color:var(--title-navy);letter-spacing:.5px}

  .benefit{position:absolute;left:0;width:848px;height:164px}
  .benefit-ring{position:absolute;left:40px;top:0;width:200px;height:164px}
  .benefit-panel{position:absolute;left:186px;top:0;width:548px;height:164px;background:var(--panel)}
  .benefit-bar{position:absolute;left:734px;top:0;width:38px;height:164px}
  .benefit-heading{position:absolute;left:192px;top:3px;font-size:28px;font-weight:400;line-height:1}
  .benefit-list{position:absolute;left:228px;list-style:none;font-size:14.6px;line-height:19px;color:var(--ink)}

  .b1{top:220px}.b1 .benefit-bar{background:var(--c1)}.b1 .benefit-heading{color:var(--c1)}.b1 .benefit-list{top:42px}
  .b2{top:388px}.b2 .benefit-bar{background:var(--c2)}.b2 .benefit-heading{color:var(--c2-head)}.b2 .benefit-list{top:48px}
  .b3{top:556px}.b3 .benefit-bar{background:var(--c3)}.b3 .benefit-heading{color:var(--c3)}.b3 .benefit-list{top:70px}
  .b4{top:724px}.b4 .benefit-bar{background:var(--c4)}.b4 .benefit-heading{color:var(--c4)}.b4 .benefit-list{top:42px;left:236px}
  .b5{top:892px}.b5 .benefit-bar{background:var(--c5)}.b5 .benefit-heading{color:var(--c5)}.b5 .benefit-list{top:48px;left:236px}

  .closing{position:absolute;left:0;top:1068px;width:848px;height:94px;background:var(--band);color:#fff;font-size:17.5px;line-height:24px;padding:10px 0 0 74px}
  .footer{position:absolute;left:0;top:1162px;width:848px;height:38px;background:var(--footer);color:#fff;text-align:center;font-size:17px;font-weight:700;line-height:38px}
</style>
</head>
<body>

<header class="header">
  <div class="brand">
    <div class="brand-mark"><span class="brand-dot"></span><span class="brand-name">RQ7T</span></div>
    <div class="brand-company">RIDGEVIEW QUARTZ ELECTRONICS</div>
    <div class="brand-tagline">STRATEGIC SUPPLY SOLUTIONS</div>
  </div>

  <div class="contact contact-web">
    <span class="icon"><svg width="18" height="18" viewBox="0 0 20 20" fill="none" stroke="#fff" stroke-width="1.6"><circle cx="10" cy="10" r="8"/><ellipse cx="10" cy="10" rx="3.5" ry="8"/><path d="M2 10h16M3.5 6h13M3.5 14h13"/></svg></span>
    <span>www.rq7t-example.com</span>
  </div>
  <div class="contact contact-mail">
    <span class="icon"><svg width="16" height="12" viewBox="0 0 16 12"><rect x="0" y="0" width="16" height="12" fill="#fff"/><path d="M0 0l8 7 8-7" fill="none" stroke="#111" stroke-width="1.5"/></svg></span>
    <span>sales@rq7t-example.com</span>
  </div>
  <div class="contact contact-addr">
    <span class="icon"><svg width="18" height="16" viewBox="0 0 18 16"><path d="M9 1L1 8h2.5v7h4v-4h3v4h4V8H17z" fill="#fff"/></svg></span>
    <span>1480 Larchmont Ave.<br>Fairhaven, PA 17990</span>
  </div>
  <div class="contact contact-phone">
    <span class="icon"><svg width="16" height="16" viewBox="0 0 24 24"><path fill="#fff" d="M6.6 10.8a15.1 15.1 0 006.6 6.6l2.2-2.2c.3-.3.7-.4 1-.2 1.1.4 2.3.6 3.6.6.6 0 1 .4 1 1V20c0 .6-.4 1-1 1A17 17 0 013 4c0-.6.4-1 1-1h3.5c.6 0 1 .4 1 1 0 1.2.2 2.4.6 3.6.1.3 0 .7-.2 1z"/></svg></span>
    <span>800.555.0142</span>
  </div>
</header>

<div class="rule-thick"></div>
<div class="rule-thin"></div>

<h1 class="title">VMI BENEFITS</h1>

<section class="benefit b1">
  <div class="benefit-panel"></div>
  <div class="benefit-bar"></div>
  <svg class="benefit-ring" viewBox="0 0 200 164" aria-hidden="true">
    <path d="M150 18 A86 86 0 1 0 150 146" fill="none" stroke="var(--c1-ring)" stroke-width="16"/>
    <path d="M38 82a64 64 0 0 1 128 0z" fill="var(--c1-dark)"/>
    <path d="M38 82a64 64 0 0 0 128 0z" fill="var(--c1)"/>
    <text x="102" y="100" text-anchor="middle" font-size="50" fill="#fff" font-family="Source Sans 3, sans-serif">1</text>
  </svg>
  <h2 class="benefit-heading">Risk management</h2>
  <ul class="benefit-list">
    <li>Identification of Items and values that are sole sourced</li>
    <li>Ongoing plans to reduce exposure to sole sourced items</li>
    <li>Schedule planning to eliminate freight and outages</li>
    <li>Reducing the hidden costs of forecasting errors</li>
    <li>(NOTE: With us managing the point of use we can more accurately forecast)</li>
    <li>Managing ever shortening of product lifecycles, minimizing obsolescence</li>
  </ul>
</section>

<section class="benefit b2">
  <div class="benefit-panel"></div>
  <div class="benefit-bar"></div>
  <svg class="benefit-ring" viewBox="0 0 200 164" aria-hidden="true">
    <path d="M150 18 A86 86 0 1 0 150 146" fill="none" stroke="var(--c2-ring)" stroke-width="16"/>
    <path d="M38 82a64 64 0 0 1 128 0z" fill="var(--c2-dark)"/>
    <path d="M38 82a64 64 0 0 0 128 0z" fill="var(--c2)"/>
    <text x="102" y="100" text-anchor="middle" font-size="50" fill="#fff" font-family="Source Sans 3, sans-serif">2</text>
  </svg>
  <h2 class="benefit-heading">Zero inventory exposure</h2>
  <ul class="benefit-list">
    <li>Minimized or zero inventory on commodity items</li>
    <li>Greatly reducing the Weighted Cost of Capital (WACC)</li>
    <li>Reduced WACC can help in calculating Hurdle Rates</li>
  </ul>
</section>

<section class="benefit b3">
  <div class="benefit-panel"></div>
  <div class="benefit-bar"></div>
  <svg class="benefit-ring" viewBox="0 0 200 164" aria-hidden="true">
    <path d="M150 18 A86 86 0 1 0 150 146" fill="none" stroke="var(--c3-ring)" stroke-width="16"/>
    <path d="M38 82a64 64 0 0 1 128 0z" fill="var(--c3-dark)"/>
    <path d="M38 82a64 64 0 0 0 128 0z" fill="var(--c3)"/>
    <text x="102" y="100" text-anchor="middle" font-size="50" fill="#fff" font-family="Source Sans 3, sans-serif">3</text>
  </svg>
  <h2 class="benefit-heading">True point of use billing</h2>
  <ul class="benefit-list">
    <li>Allows for better tracking and allocation of expenses from a job-job basis</li>
  </ul>
</section>

<section class="benefit b4">
  <div class="benefit-panel"></div>
  <div class="benefit-bar"></div>
  <svg class="benefit-ring" viewBox="0 0 200 164" aria-hidden="true">
    <path d="M150 18 A86 86 0 1 0 150 146" fill="none" stroke="var(--c4-ring)" stroke-width="16"/>
    <path d="M38 82a64 64 0 0 1 128 0z" fill="var(--c4-dark)"/>
    <path d="M38 82a64 64 0 0 0 128 0z" fill="var(--c4)"/>
    <text x="102" y="100" text-anchor="middle" font-size="50" fill="#fff" font-family="Source Sans 3, sans-serif">4</text>
  </svg>
  <h2 class="benefit-heading">Custom labeling</h2>
  <ul class="benefit-list">
    <li>Including things like customer part numbers, exp dates,</li>
    <li>internal hazmat codes</li>
    <li>Insures accurate processes with current materials</li>
    <li>Helps to meet 5S requirements</li>
    <li>Required for certain audits</li>
  </ul>
</section>

<section class="benefit b5">
  <div class="benefit-panel"></div>
  <div class="benefit-bar"></div>
  <svg class="benefit-ring" viewBox="0 0 200 164" aria-hidden="true">
    <path d="M150 18 A86 86 0 1 0 150 146" fill="none" stroke="var(--c5-ring)" stroke-width="16"/>
    <path d="M38 82a64 64 0 0 1 128 0z" fill="var(--c5-dark)"/>
    <path d="M38 82a64 64 0 0 0 128 0z" fill="var(--c5-ring)"/>
    <text x="102" y="100" text-anchor="middle" font-size="50" fill="#fff" font-family="Source Sans 3, sans-serif">5</text>
  </svg>
  <h2 class="benefit-heading">Lot tracking/Shelf life</h2>
  <ul class="benefit-list">
    <li>Active assistance in managing Date Codes/Lot Tracking</li>
    <li>Shortened shelf life products identified and managed</li>
    <li>Plain statement of expiration dates on products.</li>
    <li>calculation are not required</li>
  </ul>
</section>

<div class="closing">
  Taken as whole we can help calculate TRUE management and landed costs of products.<br>
  Focusing only on the price of items is like looking at just the exposed part of an iceberg.<br>
  Let RQ7T help you to see what’s underneath
</div>

<footer class="footer">www.rq7t-example.com</footer>

</body>
</html>
```